Velvet comb home studio

VELVET COMB.....at fox valley ,Wahroonga is a home hairdressing studio.
Hair services from a peaceful setting.
Quality colours and products.
free consultation prior to making appointment.
Easy and convenient after hours hair appointments.
Qualified hairdresser with over 15 years experience.
Specialise in foiling,balayage,ombre colour,tints,style cutting and blowdrying.
20 % off for new clients(colour services)
sms or call for 0491302667 for a quote.
Updates
im sorry guys but i has to re do alot of the photos. i would like something that looks elegant and classy.i will post an example of a flier style i like Added Wednesday, April 27, 2016
Project Deadline Extended Reason: im sorry i have decided i needed better photographs. please design again...i will choose someone before the deadline. please an elegant design will be great Added Wednesday, April 27, 2016
Target Market(s)
18-60 year olds
Industry/Entity Type
Hair
Requirements
Must have
- Must say home hairdressing studio
- Must say Velvet Comb at Fox Valley Wahroonga
- Must say phone number
Nice to have
- Modern but still classy and elegant
- Try to incorporate any photos which I have uploaded that looks best

```html
<!DOCTYPE html>
<html lang="en">
<head>
<meta charset="utf-8">
<title>Velvet Comb – Home Hairdressing Studio Flyer</title>
<link rel="stylesheet" href="https://fonts.googleapis.com/css2?family=Federo&family=Josefin+Sans:wght@700&family=Quicksand:wght@500&family=Noto+Serif:ital@1&family=Playfair+Display:wght@500&family=Montserrat:wght@400;500&display=swap">
<style>
  :root {
    --page-bg: #e8e3db;
    --paper: #ffffff;
    --brand-pink: #e0148a;
    --ink: #141414;
    --grey: #8a8a8a;
    --purple: #9a3c98;
    --gold-light: #f6d98a;
    --gold: #e2b04f;
    --gold-deep: #c98a2e;
    --orange: #e88a3a;
    --cream: #f3e3cf;
    --tan: #d9b892;
  }
  * { margin: 0; padding: 0; box-sizing: border-box; }
  html, body {
    width: 1200px; height: 1200px; overflow: hidden;
    background: var(--page-bg);
  }
  .flyer {
    position: absolute; left: 0; top: 176px;
    width: 1200px; height: 848px;
    background: var(--paper);
    overflow: hidden;
    box-shadow: 0 10px 30px rgba(0,0,0,.25);
  }
  .art { position: absolute; inset: 0; }

  .brand-name {
    position: absolute; left: 36px; top: 6px;
    font: 400 110px/1 "Federo", sans-serif;
    color: var(--brand-pink);
    letter-spacing: -1px;
  }
  .brand-sub {
    position: absolute; left: 36px; top: 140px; width: 398px;
    display: flex; align-items: center; justify-content: space-between;
  }
  .brand-sub .flourish {
    width: 100px; height: 20px; border-radius: 10px;
    background: linear-gradient(90deg, rgba(240,205,130,.2), var(--gold-light), rgba(240,205,130,.2));
  }
  .brand-sub .word {
    font: 400 62px/1 "Federo", sans-serif;
    color: var(--ink);
  }

  .experience { position: absolute; left: 86px; top: 222px; display: flex; align-items: flex-end; }
  .experience .num {
    font: 400 84px/1 "Federo", sans-serif; color: var(--brand-pink);
  }
  .experience .label {
    margin: 0 0 24px 18px;
    font: 500 16px/1 "Montserrat", sans-serif;
    letter-spacing: 4.4px; color: var(--grey);
  }

  .services-title {
    position: absolute; left: 56px; top: 330px;
    font: 700 38px/1 "Josefin Sans", sans-serif;
    letter-spacing: 3px; color: var(--purple);
  }
  .services {
    position: absolute; left: 56px; top: 378px; list-style: none;
  }
  .services li {
    display: flex; align-items: center; height: 36px;
    font: 500 27px/1 "Quicksand", sans-serif;
    letter-spacing: 2.2px; color: var(--ink);
  }
  .services li svg { width: 18px; height: 18px; margin-right: 12px; }

  .tagline {
    position: absolute; left: 59px; top: 606px;
    font: italic 30px/35px "Noto Serif", serif;
    letter-spacing: 2px; color: var(--brand-pink);
  }
  .tagline span { display: block; }
  .tagline span + span { padding-left: 138px; }

  .studio-line {
    position: absolute; left: 59px; top: 684px;
    font: 500 14px/1 "Montserrat", sans-serif;
    letter-spacing: 1px; color: var(--grey);
  }

  .contact { position: absolute; left: 51px; top: 712px; width: 590px; height: 120px; }
  .contact svg { position: absolute; inset: 0; }
  .contact .prompt {
    position: absolute; left: 220px; top: 16px;
    font: 400 21px/1 "Montserrat", sans-serif; color: var(--ink);
  }
  .contact .phone {
    position: absolute; left: 218px; top: 38px;
    font: 500 56px/1 "Playfair Display", serif;
    font-variant-numeric: lining-nums;
    letter-spacing: 1px; color: var(--ink);
  }
</style>
</head>
<body>
<main class="flyer">
  <svg class="art" viewBox="0 0 1200 848" width="1200" height="848">
    <defs>
      <linearGradient id="gold-strip" x1="0" x2="1">
        <stop offset="0" stop-color="#e6b65a"/>
        <stop offset=".5" stop-color="#f7dc8e"/>
        <stop offset="1" stop-color="#d9a648"/>
      </linearGradient>
      <linearGradient id="gold-ring" x1="0" y1="0" x2="1" y2="1">
        <stop offset="0" stop-color="#f8e09a"/>
        <stop offset=".5" stop-color="#d9a446"/>
        <stop offset="1" stop-color="#f4d07e"/>
      </linearGradient>
      <linearGradient id="orange-ring" x1="0" y1="0" x2="1" y2="1">
        <stop offset="0" stop-color="#f2a34c"/>
        <stop offset=".6" stop-color="#f7cf86"/>
        <stop offset="1" stop-color="#e98a36"/>
      </linearGradient>
      <radialGradient id="hero-tones" cx=".6" cy=".45" r=".7">
        <stop offset="0" stop-color="#c79a78"/>
        <stop offset=".45" stop-color="#7a4f33"/>
        <stop offset="1" stop-color="#3a2416"/>
      </radialGradient>
      <radialGradient id="red-tones"><stop offset="0" stop-color="#d98a5e"/><stop offset="1" stop-color="#8a3418"/></radialGradient>
      <radialGradient id="brunette-tones"><stop offset="0" stop-color="#e8cdb8"/><stop offset="1" stop-color="#6b4632"/></radialGradient>
      <radialGradient id="copper-tones"><stop offset="0" stop-color="#e6a07a"/><stop offset="1" stop-color="#3a2a24"/></radialGradient>
      <radialGradient id="room-tones"><stop offset="0" stop-color="#f2efe9"/><stop offset="1" stop-color="#b8a48e"/></radialGradient>
      <radialGradient id="portrait-tones"><stop offset="0" stop-color="#d6b89a"/><stop offset="1" stop-color="#2f4a5c"/></radialGradient>
    </defs>

    <path d="M598 0 C 440 160, 410 620, 900 848 L1200 848 L1200 0 Z" fill="var(--cream)"/>
    <path d="M608 0 C 460 160, 432 610, 915 848 L1200 848 L1200 0 Z" fill="var(--tan)"/>
    <path d="M620 0 C 478 160, 452 600, 930 848 L1200 848 L1200 0 Z" fill="#f1e6d8"/>

    <path d="M636 0 C 500 160, 474 590, 946 848 L1162 848 L1162 0 Z"
          fill="url(#hero-tones)" role="img" aria-label="Photo of a model with long, glossy brunette hair"/>

    <rect x="1162" y="0" width="38" height="848" fill="url(#gold-strip)"/>

    <g stroke-width="7">
      <circle cx="551" cy="175" r="86" fill="url(#red-tones)" stroke="url(#orange-ring)" role="img" aria-label="Photo of long red curly hair"/>
      <circle cx="525" cy="392" r="89" fill="url(#brunette-tones)" stroke="url(#gold-ring)" role="img" aria-label="Photo of colour swatches beside brunette hair"/>
      <circle cx="581" cy="602" r="89" fill="url(#copper-tones)" stroke="url(#orange-ring)" role="img" aria-label="Photo of a copper bob haircut"/>
    </g>

    <g stroke="url(#gold-ring)" stroke-width="7">
      <circle cx="1088" cy="113" r="90" fill="url(#room-tones)" role="img" aria-label="Photo of studio product shelves"/>
      <circle cx="1088" cy="324" r="90" fill="url(#room-tones)" role="img" aria-label="Photo of the styling station"/>
      <circle cx="1088" cy="536" r="90" fill="url(#room-tones)" role="img" aria-label="Photo of the studio waiting area"/>
      <circle cx="1088" cy="750" r="90" fill="url(#portrait-tones)" role="img" aria-label="Portrait photo of the hairdresser"/>
    </g>
  </svg>

  <h1 class="brand-name">Velvet</h1>
  <div class="brand-sub">
    <span class="flourish" role="img" aria-label="Gold flourish"></span>
    <span class="word">COMB</span>
    <span class="flourish" role="img" aria-label="Gold flourish"></span>
  </div>

  <div class="experience">
    <span class="num">15</span>
    <span class="label">YEARS EXPERIENCE</span>
  </div>

  <h2 class="services-title">SPACIALIZE IN</h2>
  <ul class="services">
    <li><svg viewBox="0 0 18 18"><g fill="none" stroke="#e2a34c" stroke-width="1.6"><circle cx="4" cy="13" r="2.4"/><circle cx="9" cy="15" r="2.4"/><path d="M5.8 11.5 L15 3 M10 12.8 L12 4"/></g></svg>Foiling</li>
    <li><svg viewBox="0 0 18 18"><g fill="none" stroke="#e2a34c" stroke-width="1.6"><circle cx="4" cy="13" r="2.4"/><circle cx="9" cy="15" r="2.4"/><path d="M5.8 11.5 L15 3 M10 12.8 L12 4"/></g></svg>Balayage</li>
    <li><svg viewBox="0 0 18 18"><g fill="none" stroke="#e2a34c" stroke-width="1.6"><circle cx="4" cy="13" r="2.4"/><circle cx="9" cy="15" r="2.4"/><path d="M5.8 11.5 L15 3 M10 12.8 L12 4"/></g></svg>Tints</li>
    <li><svg viewBox="0 0 18 18"><g fill="none" stroke="#e2a34c" stroke-width="1.6"><circle cx="4" cy="13" r="2.4"/><circle cx="9" cy="15" r="2.4"/><path d="M5.8 11.5 L15 3 M10 12.8 L12 4"/></g></svg>Ombre Colour</li>
    <li><svg viewBox="0 0 18 18"><g fill="none" stroke="#e2a34c" stroke-width="1.6"><circle cx="4" cy="13" r="2.4"/><circle cx="9" cy="15" r="2.4"/><path d="M5.8 11.5 L15 3 M10 12.8 L12 4"/></g></svg>Style Cutting</li>
    <li><svg viewBox="0 0 18 18"><g fill="none" stroke="#e2a34c" stroke-width="1.6"><circle cx="4" cy="13" r="2.4"/><circle cx="9" cy="15" r="2.4"/><path d="M5.8 11.5 L15 3 M10 12.8 L12 4"/></g></svg>Blowdrying</li>
  </ul>

  <p class="tagline"><span>more affordable</span><span>than a hair salon...</span></p>

  <p class="studio-line">Home hairdressing studio · Velvet Comb at Fox Valley Wahroonga</p>

  <div class="contact">
    <svg viewBox="0 0 590 120" width="590" height="120">
      <defs>
        <linearGradient id="pill-gold" x1="0" x2="1">
          <stop offset="0" stop-color="#e9a94a"/>
          <stop offset=".5" stop-color="#f3cf80"/>
          <stop offset="1" stop-color="#e6b55a"/>
        </linearGradient>
      </defs>
      <path d="M90 64 C 130 60, 150 52, 180 32 C 200 12, 220 2, 250 2 L538 2 A52 52 0 0 1 538 106 L250 106 C 200 106, 175 82, 150 72 C 130 66, 110 68, 90 72 Z" fill="url(#pill-gold)"/>
      <circle cx="47" cy="70" r="43" fill="#fff" stroke="var(--orange)" stroke-width="6"/>
      <circle cx="47" cy="70" r="32" fill="#fbe9d6"/>
      <g fill="var(--orange)">
        <path d="M28 61 C 30 51, 64 51, 66 61 L66 65 L58 65 L57 60 C 52 58, 42 58, 37 60 L36 65 L28 65 Z"/>
        <path d="M36 67 L58 67 L62 85 L32 85 Z"/>
      </g>
      <circle cx="47" cy="76" r="5" fill="#fff"/>
    </svg>
    <p class="prompt">sms or call Marissa</p>
    <p class="phone">0491302667</p>
  </div>
</main>
</body>
</html>
```